Family Brewery needs a label design for the four different types of beer.

We need a label design for two beer bottle sizes (500 and 700 ml. )
The label design should include the family monogram and company logo, as it would be a corporate gift for the new year from our CEO to business partners and clients. We have one request for showing the company logo on bottle. As it would be the new year edition, we would like to see design "adaptive" in case we would like to keep it after the holidays on an ongoing basis. Our main company direction is design and manufacture of cooling equipment for ice rinks, so it would be fine but not necessary to see design related to our business (if you would like to check the company, there is our website - www.velmarik.ru)
Labels on bottles should be in the same style but vary depending on the variety and taste of beer.
Types of bear
-Pilzner ( 4.4 % of alcohol)
-Honig Pilsner(5.2 % of alcohol)
-Wiener Ale ( 4.7 % of alcohol)
-Weissbier (5.6 % of alcohol)
If you have any questions just message me and i will answer as soon as possible.
Files attached contain the family monogram, company logo ( velmarik ), picture of beer bottles that would be in usage.

```html
<!DOCTYPE html>
<html lang="en">
<head>
<meta charset="utf-8">
<title>Velmarik Family Brewery – Label Series</title>
<link href="https://fonts.googleapis.com/css2?family=Oswald:wght@500;600&family=Rye&family=Holtwood+One+SC&family=Grenze+Gotisch:wght@600&display=swap" rel="stylesheet">
<style>
  :root{
    --bg-top:#ffffff;
    --bg-bottom:#cfcfcf;
    --honig:#ec9a2a;
    --honig-light:#f7c25e;
    --wiener:#c4202c;
    --wiener-light:#e24a4f;
    --pilzner:#3e7744;
    --pilzner-light:#6a9e62;
    --weiss:#1d6db6;
    --weiss-light:#4d9ad8;
    --panel:#ffffff;
    --ink:#2a2a2a;
    --mark-red:#e2202a;
    --monogram-tone:#8e8e8e;
  }
  *{margin:0;padding:0;box-sizing:border-box}
  html,body{width:1200px;height:886px;overflow:hidden}
  body{
    background:linear-gradient(180deg,var(--bg-top) 0%,var(--bg-top) 70%,var(--bg-bottom) 100%);
    font-family:"Oswald",sans-serif;
  }
  .defs{position:absolute;width:0;height:0}
  .label-row{
    position:absolute;left:0;top:230px;width:1200px;height:420px;
    display:flex;justify-content:space-evenly;
  }
  .label{
    position:relative;width:260px;height:420px;
    box-shadow:0 2px 6px rgba(0,0,0,.18);
  }
  .label--honig{background:radial-gradient(circle at 50% 45%,var(--honig-light),var(--honig) 70%)}
  .label--wiener{background:radial-gradient(circle at 50% 45%,var(--wiener-light),var(--wiener) 70%)}
  .label--pilzner{background:radial-gradient(circle at 50% 45%,var(--pilzner-light),var(--pilzner) 70%)}
  .label--weiss{background:radial-gradient(circle at 50% 45%,var(--weiss-light),var(--weiss) 70%)}
  .label__panel{position:absolute;left:30px;top:40px;width:200px;height:340px}
  .label__monogram{
    position:absolute;left:80px;top:56px;width:100px;height:20px;
    border-radius:10px;
    background:var(--monogram-tone);
  }
  .label__style{
    position:absolute;left:44px;top:96px;width:172px;text-align:center;
    color:var(--ink);line-height:36px;white-space:nowrap;overflow:hidden;
  }
  .style--honig{font-family:"Rye",serif;font-size:15px}
  .style--wiener{font-family:"Holtwood One SC",serif;font-size:16px}
  .style--pilzner{font-family:"Oswald",sans-serif;font-weight:600;font-size:31px;letter-spacing:2px}
  .style--weiss{font-family:"Grenze Gotisch",serif;font-weight:600;font-size:32px}
  .label__mark{
    position:absolute;left:85px;top:142px;width:90px;height:90px;
    border-radius:50%;background:var(--mark-red);
  }
  .label__brand{
    position:absolute;left:30px;top:248px;width:200px;text-align:center;
    color:var(--ink);font-weight:600;font-size:30px;line-height:36px;letter-spacing:1px;
  }
  .label__brand-local{
    position:absolute;left:48px;top:288px;width:164px;
    display:flex;align-items:center;gap:8px;
    color:var(--ink);font-weight:500;font-size:12px;
  }
  .label__brand-local::before,.label__brand-local::after{
    content:"";flex:1;height:1.5px;background:var(--ink);
  }
  .label__facts{
    position:absolute;left:30px;top:315px;width:200px;text-align:center;
    color:var(--ink);font-weight:500;font-size:12px;letter-spacing:.5px;
  }
  .label__facts .sep{display:inline-block;width:1px;height:14px;background:var(--ink);vertical-align:middle;margin:0 8px}
  .label__facts .star{font-size:9px;margin:0 10px}
</style>
</head>
<body>
<svg class="defs" aria-hidden="true">
  <defs>
    <symbol id="panel-shape" viewBox="0 0 200 340">
      <path d="M0,42 Q0,22 20,22 L55,22 Q64,0 100,0 Q136,0 145,22 L180,22 Q200,22 200,42 L200,305 Q200,340 165,340 L35,340 Q0,340 0,305 Z" fill="#ffffff"/>
      <path d="M8,48 Q8,30 26,30 L60,30 Q69,8 100,8 Q131,8 140,30 L174,30 Q192,30 192,48 L192,302 Q192,332 162,332 L38,332 Q8,332 8,302 Z" fill="none" stroke="#2a2a2a" stroke-width="1.5"/>
    </symbol>
  </defs>
</svg>

<main class="label-row">
  <section class="label label--honig">
    <svg class="label__panel"><use href="#panel-shape"/></svg>
    <div class="label__monogram" role="img" aria-label="Family monogram with crown and flourishes"></div>
    <h2 class="label__style style--honig">HONIG PILSNER</h2>
    <div class="label__mark"></div>
    <p class="label__brand">VELMARIK</p>
    <p class="label__brand-local">ВЕЛМАРИК</p>
    <p class="label__facts"><span class="star">★</span>5.2%<span class="sep"></span>500ml<span class="star">★</span></p>
  </section>

  <section class="label label--wiener">
    <svg class="label__panel"><use href="#panel-shape"/></svg>
    <div class="label__monogram" role="img" aria-label="Family monogram with crown and flourishes"></div>
    <h2 class="label__style style--wiener">WIENER ALE</h2>
    <div class="label__mark"></div>
    <p class="label__brand">VELMARIK</p>
    <p class="label__brand-local">ВЕЛМАРИК</p>
    <p class="label__facts"><span class="star">★</span>4.7%<span class="sep"></span>500ml<span class="star">★</span></p>
  </section>

  <section class="label label--pilzner">
    <svg class="label__panel"><use href="#panel-shape"/></svg>
    <div class="label__monogram" role="img" aria-label="Family monogram with crown and flourishes"></div>
    <h2 class="label__style style--pilzner">PILZNER</h2>
    <div class="label__mark"></div>
    <p class="label__brand">VELMARIK</p>
    <p class="label__brand-local">ВЕЛМАРИК</p>
    <p class="label__facts"><span class="star">★</span>4.4%<span class="sep"></span>500ml<span class="star">★</span></p>
  </section>

  <section class="label label--weiss">
    <svg class="label__panel"><use href="#panel-shape"/></svg>
    <div class="label__monogram" role="img" aria-label="Family monogram with crown and flourishes"></div>
    <h2 class="label__style style--weiss">Weissbier</h2>
    <div class="label__mark"></div>
    <p class="label__brand">VELMARIK</p>
    <p class="label__brand-local">ВЕЛМАРИК</p>
    <p class="label__facts"><span class="star">★</span>5.6%<span class="sep"></span>500ml<span class="star">★</span></p>
  </section>
</main>
</body>
</html>
```